Quorvane Exploration and Production

We need a powerpoint design for a new exploration company. I would like to either use black logo or change color to a cardinal color. We explore oil and gas exploration. We would like to see designs with a cardinal color. The ppt would be a universal ppt used for presenting deals.

```html
<!DOCTYPE html>
<html lang="en">
<head>
<meta charset="utf-8">
<title>Quorvane Exploration and Production – Deck Overview</title>
<link rel="stylesheet" href="https://fonts.googleapis.com/css2?family=Montserrat:wght@400;500;600;700;800&display=swap">
<style>
:root{
  --cardinal:#c8102e;
  --ink:#111111;
  --navy:#1d3d66;
  --blue:#1f6fb2;
  --grey:#7a7a7a;
  --muted:#8c8c8c;
  --line:#d9d9d9;
  --paper:#ffffff;
  --bg:#ffffff;
}
*{margin:0;padding:0;box-sizing:border-box}
html,body{width:1042px;height:1200px;overflow:hidden;background:var(--bg)}
body{position:relative;font-family:"Montserrat",sans-serif;color:var(--ink)}
.slide{position:absolute;width:224px;height:126px;background:var(--paper);overflow:hidden;box-shadow:3px 4px 8px rgba(0,0,0,.28)}
.abs{position:absolute}
.rule{position:absolute;left:18px;right:18px;top:6px;height:.4px;background:#999}
.brand{position:absolute;right:18px;top:3px;font-size:3.4px;font-weight:800;letter-spacing:.3px;background:var(--paper);padding-left:2px}
.brand.light{color:#fff;background:none}
.foot{position:absolute;left:12px;bottom:4px;font-size:2.2px;color:#aaa}
.pg{position:absolute;right:12px;bottom:4px;font-size:2.2px;color:#aaa}
.title{position:absolute;left:0;right:0;top:16px;text-align:center;font-size:9.5px;font-weight:500}
.ltitle{position:absolute;font-size:9.5px;font-weight:500;line-height:.95}
.cap{font-size:2.8px;font-weight:700;letter-spacing:.5px;text-transform:uppercase}
.para{font-size:2.3px;line-height:1.5;color:var(--grey);text-align:justify}
.center{text-align:center}
.num{font-size:11px;font-weight:700}
.band-top{position:absolute;left:0;right:0;top:0;height:10px;background:var(--ink)}
.band-bot{position:absolute;left:0;right:0;bottom:0;height:10px;background:var(--ink)}
.photo-rig{background:linear-gradient(180deg,#7fa8d4 0%,#b9cfe6 55%,#a08566 70%,#6e5a42 100%)}
.photo-grey{background:linear-gradient(180deg,#cfcfcf 0%,#9a9a9a 55%,#5a5a5a 75%,#2c2c2c 100%)}
.photo-field{background:linear-gradient(180deg,#a9c4e0 0%,#d8e2ea 50%,#b79f80 65%,#8a6f52 100%)}
.photo-crew{background:linear-gradient(180deg,#9fbede 0%,#c8cfd4 55%,#b6a27a 100%)}
.icon{width:7px;height:7px}
.icon use,.icon path,.icon circle,.icon rect{stroke:var(--ink);fill:none;stroke-width:1}
.hidden{position:absolute;width:0;height:0}
table.data{position:absolute;left:12px;top:32px;width:200px;border-collapse:collapse;font-size:2.8px}
table.data td,table.data th{height:6.4px;text-align:center;border-bottom:.3px solid #ccc;font-weight:400}
table.data th{background:var(--cardinal);color:#fff}
table.data td:first-child{text-align:left;padding-left:2px}
table.data tr.total td{background:var(--ink);color:#fff}
.phase{position:absolute;left:8px;width:54px;height:5px;background:var(--cardinal);color:#fff;font-size:2.6px;padding-left:2px;line-height:5px}
.phase.dark{background:var(--ink)}
</style>
</head>
<body>

<svg class="hidden" aria-hidden="true">
  <defs>
    <symbol id="i-wrench" viewBox="0 0 10 10"><path d="M2 8 L6 4 M6 4 A2 2 0 1 1 8 2" /></symbol>
    <symbol id="i-home" viewBox="0 0 10 10"><path d="M1.5 5 L5 1.5 L8.5 5 M2.5 4.5 V8.5 H7.5 V4.5 M4.2 8.5 V6.5 H5.8 V8.5" /></symbol>
    <symbol id="i-chat" viewBox="0 0 10 10"><path d="M2 6.5 A3.5 2.8 0 1 1 4 7.5 L1.5 8.5 Z" /></symbol>
    <symbol id="i-check" viewBox="0 0 10 10"><circle cx="5" cy="5" r="4"/><path d="M3 5 L4.5 6.5 L7 3.5"/></symbol>
    <symbol id="i-funnel" viewBox="0 0 10 10"><path d="M1.5 2 H8.5 L5.8 5.5 V8.5 L4.2 7.5 V5.5 Z"/></symbol>
    <symbol id="i-box" viewBox="0 0 10 10"><rect x="2" y="3.5" width="6" height="5"/><path d="M1.5 3.5 H8.5 M4 2 H6"/></symbol>
    <symbol id="i-gear" viewBox="0 0 10 10"><circle cx="5" cy="5" r="2"/><circle cx="5" cy="5" r="3.8"/></symbol>
    <symbol id="i-screen" viewBox="0 0 10 10"><rect x="1.5" y="2" width="7" height="5"/><path d="M4 8.5 H6"/></symbol>
  </defs>
</svg>

<!-- Row 1 -->
<section class="slide" style="left:36px;top:45px">
  <div class="band-top"></div>
  <div class="abs photo-rig" role="img" aria-label="Photo of an oil drilling rig under a blue sky" style="left:120px;top:10px;width:104px;height:106px;clip-path:polygon(30% 0,100% 0,100% 100%,0 100%)"></div>
  <div class="abs" style="left:17px;top:39px;font-size:4px;font-weight:800;letter-spacing:.3px">QUORVANE</div>
  <div class="abs" style="left:48px;top:37px;font-size:5.4px;font-weight:800;line-height:1">WE EXPLORE<br>OIL AND GAS<br>EXPLORATION</div>
  <div class="abs" style="left:17px;top:64px;font-size:5.2px;font-weight:700">Subtitle Presentation goes here</div>
  <div class="abs" style="left:17px;top:73px;font-size:4.6px">John Merrow</div>
  <div class="abs" style="left:17px;top:79.5px;font-size:2.8px">Ceo - Founder</div>
  <div class="abs" style="left:17px;top:88px;font-size:3.8px">August 2024</div>
  <div class="band-bot"></div>
  <span class="foot" style="color:#666">©2024 Quorvane. All rights reserved. Confidential information.</span>
</section>

<section class="slide" style="left:284px;top:45px">
  <div class="abs photo-field" role="img" aria-label="Faded photo of an oil field landscape" style="left:70px;top:0;right:0;bottom:0;opacity:.45"></div>
  <div class="ltitle" style="left:16px;top:20px;font-size:9px">About<br><b style="font-weight:800">QUORVANE</b></div>
  <p class="abs para" style="left:16px;top:44px;width:64px">Our team explores new oil and gas fields with care, clear data and steady work on every site we open across the region.</p>
  <p class="abs para" style="left:16px;top:70px;width:64px">We plan each well with safety first, share results with partners and keep every deal simple to follow from start to end.</p>
  <div class="band-bot"></div>
  <span class="foot" style="color:#666">©2024 Quorvane. All rights reserved. Confidential information.</span>
</section>

<section class="slide" style="left:533px;top:45px">
  <div class="rule"></div><span class="brand">QUORVANE</span>
  <div class="ltitle" style="left:16px;top:19px">Today<br>Agenda</div>
  <div class="abs" style="left:17px;top:48px;font-size:3.2px;color:#555">August 14 , 2024</div>
  <div class="abs" style="left:16px;top:68px;width:196px;display:flex;justify-content:space-between">
    <div style="width:32px"><div style="font-size:2.4px;font-weight:700">8:00 – 9:00</div><div class="cap" style="font-size:2.4px;margin-top:6px">Welcome</div><p class="para" style="margin-top:5px;text-align:left">A short note on the plan for the day.</p></div>
    <div style="width:32px"><div style="font-size:2.4px;font-weight:700">9:00 – 10:00</div><div class="cap" style="font-size:2.4px;margin-top:6px">About</div><p class="para" style="margin-top:5px;text-align:left">A short note on who we are today.</p></div>
    <div style="width:32px"><div style="font-size:2.4px;font-weight:700">11:30 – 13:00</div><div class="cap" style="font-size:2.4px;margin-top:6px">Break</div><p class="para" style="margin-top:5px;text-align:left">A short note on lunch and the pause.</p></div>
    <div style="width:32px"><div style="font-size:2.4px;font-weight:700">13:00 – 14:00</div><div class="cap" style="font-size:2.4px;margin-top:6px">Case Studies</div><p class="para" style="margin-top:5px;text-align:left">A short note on past field work.</p></div>
    <div style="width:32px"><div style="font-size:2.4px;font-weight:700">14:00 – 15:00</div><div class="cap" style="font-size:2.4px;margin-top:6px">Closing</div><p class="para" style="margin-top:5px;text-align:left">A short note on next steps ahead.</p></div>
  </div>
  <span class="foot">©2024 Quorvane. All rights reserved. Confidential information.</span><span class="pg">3</span>
</section>

<section class="slide" style="left:781px;top:45px">
  <div class="abs photo-grey" role="img" aria-label="Black and white photo of a drilling rig and site buildings" style="inset:0"></div>
  <span class="brand light" style="top:4px">QUORVANE</span>
  <svg class="abs" style="left:50px;top:48px" width="124" height="22" viewBox="0 0 124 22"><path d="M4 2 L12 11 L4 20" stroke="#111" stroke-width="2" fill="none"/><path d="M120 2 L112 11 L120 20" stroke="#111" stroke-width="2" fill="none"/></svg>
  <div class="abs" style="left:50px;top:57px;font-size:3px;font-weight:600">11:30</div>
  <div class="abs" style="left:162px;top:57px;font-size:3px;font-weight:600">13:00</div>
  <div class="abs center" style="left:70px;width:84px;top:50px;font-size:9px;font-weight:500;line-height:.95">The Break<br>time</div>
  <div class="abs" style="left:0;right:0;bottom:0;height:5px;background:#111"></div>
  <span class="foot" style="color:#ddd;bottom:1.5px">©2024 Quorvane. All rights reserved. Confidential information.</span>
</section>

<!-- Row 2 -->
<section class="slide" style="left:36px;top:186px">
  <div class="abs photo-rig" role="img" aria-label="Photo of a drilling rig in a flat field" style="inset:0"></div>
  <div class="abs" style="left:60px;top:0;right:0;bottom:0;background:linear-gradient(160deg,#1d3d66 0%,#23497a 100%);clip-path:polygon(45% 0,100% 0,100% 100%,0 100%)"></div>
  <span class="brand light">QUORVANE</span>
  <div class="abs" style="left:24px;top:56px;font-size:10px;font-weight:700;color:#fff">1</div>
  <div class="abs" style="left:92px;top:44px;font-size:9.5px;font-weight:700;color:#fff;line-height:1.15">SECTION<br>BREAK<br>SLIDE</div>
  <span class="foot" style="color:#eee">©2024 Quorvane. All rights reserved. Confidential information.</span>
</section>

<section class="slide" style="left:284px;top:186px">
  <div class="rule"></div><span class="brand">QUORVANE</span>
  <div class="title">About The project</div>
  <div class="abs center" style="left:22px;width:48px;top:36px"><div class="cap" style="font-size:2.5px">Skill Title</div><p class="para center" style="margin-top:2px">Short lines of copy about this skill.</p></div>
  <div class="abs center" style="left:154px;width:48px;top:36px"><div class="cap" style="font-size:2.5px">Skill Title</div><p class="para center" style="margin-top:2px">Short lines of copy about this skill.</p></div>
  <div class="abs center" style="left:22px;width:48px;top:93px"><div class="cap" style="font-size:2.5px">Skill Title</div><p class="para center" style="margin-top:2px">Short lines of copy about this skill.</p></div>
  <div class="abs center" style="left:154px;width:48px;top:93px"><div class="cap" style="font-size:2.5px">Skill Title</div><p class="para center" style="margin-top:2px">Short lines of copy about this skill.</p></div>
  <svg class="abs icon" style="left:82px;top:45px" viewBox="0 0 10 10"><use href="#i-funnel"/></svg>
  <svg class="abs icon" style="left:135px;top:44px" viewBox="0 0 10 10"><use href="#i-chat"/></svg>
  <svg class="abs icon" style="left:82px;top:95px" viewBox="0 0 10 10"><use href="#i-box"/></svg>
  <svg class="abs icon" style="left:135px;top:95px" viewBox="0 0 10 10"><use href="#i-gear"/></svg>
  <span class="foot">©2024 Quorvane. All rights reserved. Confidential information.</span><span class="pg">6</span>
</section>

<section class="slide" style="left:533px;top:186px">
  <div class="rule"></div><span class="brand">QUORVANE</span>
  <div class="title">The project in Numbers</div>
  <div class="abs" style="left:14px;right:14px;top:43px;display:flex;justify-content:space-between">
    <div class="center" style="width:60px"><div class="num">3.515</div><div class="cap" style="font-size:2.4px;margin-top:3px">Your Title Here</div><p class="para center" style="margin-top:3px">A short statement that explains what this figure means.</p></div>
    <div class="center" style="width:60px"><div class="num">381</div><div class="cap" style="font-size:2.4px;margin-top:3px">Your Title Here</div><p class="para center" style="margin-top:3px">A short statement that explains what this figure means.</p></div>
    <div class="center" style="width:60px"><div class="num">$85B</div><div class="cap" style="font-size:2.4px;margin-top:3px">Your Title Here</div><p class="para center" style="margin-top:3px">A short statement that explains what this figure means.</p></div>
  </div>
  <span class="foot">©2024 Quorvane. All rights reserved. Confidential information.</span><span class="pg">7</span>
</section>

<section class="slide" style="left:781px;top:186px">
  <div class="abs photo-field" role="img" aria-label="Faded photo of an oil field" style="inset:0;opacity:.35"></div>
  <div class="rule"></div><span class="brand" style="background:none">QUORVANE</span>
  <div class="title">The project in Numbers</div>
  <div class="abs" style="left:14px;right:14px;top:36px;display:flex;justify-content:space-between">
    <div class="center" style="width:60px"><svg class="icon" viewBox="0 0 10 10"><use href="#i-wrench"/></svg><div class="num">$38M</div><div class="cap" style="font-size:2.4px;margin-top:3px">Your Title Here</div><p class="para center" style="margin-top:3px">A short statement that explains what this figure means.</p></div>
    <div class="center" style="width:60px"><svg class="icon" viewBox="0 0 10 10"><use href="#i-home"/></svg><div class="num">9400</div><div class="cap" style="font-size:2.4px;margin-top:3px">Your Title Here</div><p class="para center" style="margin-top:3px">A short statement that explains what this figure means.</p></div>
    <div class="center" style="width:60px"><svg class="icon" viewBox="0 0 10 10"><use href="#i-chat"/></svg><div class="num">310</div><div class="cap" style="font-size:2.4px;margin-top:3px">Your Title Here</div><p class="para center" style="margin-top:3px">A short statement that explains what this figure means.</p></div>
  </div>
  <span class="foot">©2024 Quorvane. All rights reserved. Confidential information.</span><span class="pg">8</span>
</section>

<!-- Row 3 -->
<section class="slide" style="left:36px;top:326px">
  <div class="rule"></div><span class="brand">QUORVANE</span>
  <div class="title">Slide Process</div>
  <svg class="abs" style="left:0;top:40px" width="224" height="30" viewBox="0 0 224 30">
    <line x1="47" y1="14" x2="177" y2="14" stroke="#333" stroke-width=".4"/>
    <g fill="#fff" stroke="#333" stroke-width=".5"><circle cx="47" cy="14" r="14"/><circle cx="112" cy="14" r="14"/><circle cx="177" cy="14" r="14"/><circle cx="47" cy="28" r="2.5"/><circle cx="112" cy="28" r="2.5"/><circle cx="177" cy="28" r="2.5"/></g>
    <use href="#i-wrench" x="42" y="9" width="10" height="10" stroke="#111" fill="none"/>
    <use href="#i-home" x="107" y="9" width="10" height="10" stroke="#111" fill="none"/>
    <use href="#i-chat" x="172" y="9" width="10" height="10" stroke="#111" fill="none"/>
  </svg>
  <div class="abs" style="left:17px;right:17px;top:82px;display:flex;justify-content:space-between">
    <div class="center" style="width:56px"><div class="cap" style="font-size:2.6px">Your Title Here</div><p class="para center" style="margin-top:3px">A short line of copy that explains this step clearly.</p></div>
    <div class="center" style="width:56px"><div class="cap" style="font-size:2.6px">Your Title Here</div><p class="para center" style="margin-top:3px">A short line of copy that explains this step clearly.</p></div>
    <div class="center" style="width:56px"><div class="cap" style="font-size:2.6px">Your Title Here</div><p class="para center" style="margin-top:3px">A short line of copy that explains this step clearly.</p></div>
  </div>
  <span class="foot">©2024 Quorvane. All rights reserved. Confidential information.</span><span class="pg">9</span>
</section>

<section class="slide" style="left:284px;top:326px">
  <div class="rule"></div><span class="brand">QUORVANE</span>
  <div class="title">Three awesome Values</div>
  <svg class="abs" style="left:0;top:42px" width="224" height="56" viewBox="0 0 224 56">
    <g fill="none" stroke="#111" stroke-width=".6"><circle cx="57" cy="28" r="27"/><circle cx="112" cy="28" r="27"/><circle cx="167" cy="28" r="27"/></g>
    <use href="#i-wrench" x="52" y="10" width="10" height="10" stroke="#111" fill="none"/>
    <use href="#i-home" x="107" y="10" width="10" height="10" stroke="#111" fill="none"/>
    <use href="#i-chat" x="162" y="10" width="10" height="10" stroke="#111" fill="none"/>
  </svg>
  <div class="abs" style="left:37px;width:150px;top:70px;display:flex;justify-content:space-between">
    <div class="center" style="width:40px"><div class="cap" style="font-size:2.6px">Your Title Here</div><p class="para center" style="margin-top:3px">A short line on the value we hold.</p></div>
    <div class="center" style="width:40px"><div class="cap" style="font-size:2.6px">Your Title Here</div><p class="para center" style="margin-top:3px">A short line on the value we hold.</p></div>
    <div class="center" style="width:40px"><div class="cap" style="font-size:2.6px">Your Title Here</div><p class="para center" style="margin-top:3px">A short line on the value we hold.</p></div>
  </div>
  <span class="foot">©2024 Quorvane. All rights reserved. Confidential information.</span><span class="pg">10</span>
</section>

<section class="slide" style="left:533px;top:326px">
  <div class="rule"></div><span class="brand">QUORVANE</span>
  <div class="title">Our Members</div>
  <div class="abs" style="left:0;right:0;top:36px;display:flex;justify-content:space-around" >
    <span class="cap" style="font-size:2.6px">Team Member</span><span class="cap" style="font-size:2.6px">Team Member</span><span class="cap" style="font-size:2.6px">Team Member</span>
  </div>
  <div class="abs" style="left:0;right:0;top:44px;height:48px;display:flex;gap:1px">
    <div class="photo-crew" role="img" aria-label="Photo of a crew member in work gear at a rig site" style="flex:1"></div>
    <div class="photo-crew" role="img" aria-label="Photo of a crew member in work gear at a rig site" style="flex:1"></div>
    <div class="photo-crew" role="img" aria-label="Photo of a crew member in work gear at a rig site" style="flex:1"></div>
  </div>
  <p class="abs para center" style="left:30px;right:30px;top:102px">A short paragraph about the people who lead our field work and keep every project moving safely.</p>
  <span class="foot">©2024 Quorvane. All rights reserved. Confidential information.</span><span class="pg">11</span>
</section>

<section class="slide" style="left:781px;top:326px">
  <div class="rule"></div><span class="brand">QUORVANE</span>
  <div class="abs photo-rig" role="img" aria-label="Photo of a drilling rig" style="left:7px;top:7px;width:52px;height:52px;clip-path:polygon(50% 0,100% 50%,50% 100%,0 50%)"></div>
  <div class="abs photo-rig" role="img" aria-label="Photo of a drilling rig" style="left:57px;top:7px;width:52px;height:52px;clip-path:polygon(50% 0,100% 50%,50% 100%,0 50%)"></div>
  <div class="abs photo-field" role="img" aria-label="Photo of a dry field with a pipeline" style="left:32px;top:32px;width:52px;height:52px;clip-path:polygon(50% 0,100% 50%,50% 100%,0 50%)"></div>
  <div class="abs photo-field" role="img" aria-label="Photo of pipes laid across dry ground" style="left:57px;top:57px;width:52px;height:52px;clip-path:polygon(50% 0,100% 50%,50% 100%,0 50%)"></div>
  <div class="abs" style="left:133px;top:30px;font-size:7.5px;font-weight:500;line-height:1.15">WHAT IS<br>LOREM<br>IPSUM?</div>
  <p class="abs para" style="left:133px;top:67px;width:76px;text-align:left">Our team explores new oil and gas fields with care, clear data and steady work on every site we open. We plan each well with safety first, share results with partners and keep every deal simple to follow.</p>
  <span class="foot">©2024 Quorvane. All rights reserved. Confidential information.</span><span class="pg">12</span>
</section>

<!-- Row 4 -->
<section class="slide" style="left:36px;top:467px">
  <div class="rule" style="left:113px"></div><span class="brand">QUORVANE</span>
  <div class="abs photo-rig" role="img" aria-label="Photo of a drilling rig beside a dirt road" style="left:0;top:0;width:113px;height:126px"></div>
  <div class="abs" style="left:29px;top:42px;font-size:8.5px;font-weight:700;color:#fff;line-height:1.1">Title<br>text and<br>image<br>Slide</div>
  <div class="abs" style="left:129px;top:34px;font-size:4.6px;font-weight:500">WHAT IS LOREM IPSUM?</div>
  <p class="abs para" style="left:129px;top:45px;width:74px;text-align:left">Our team explores new oil and gas fields with care, clear data and steady work on every site we open. We plan each well with safety first, share results with partners and keep every deal simple to follow from start to end for every client.</p>
  <span class="pg">13</span>
</section>

<section class="slide" style="left:284px;top:467px">
  <div class="abs photo-rig" role="img" aria-label="Wide photo of rigs across an open field" style="left:0;right:0;top:0;height:62px"></div>
  <span class="brand light">QUORVANE</span>
  <div class="abs" style="left:12px;right:12px;top:68px;display:flex;justify-content:space-between">
    <div class="center" style="width:60px"><svg class="icon" viewBox="0 0 10 10"><use href="#i-screen"/></svg><div class="cap" style="font-size:2.6px;margin-top:2px">Your Title Here</div><p class="para" style="margin-top:3px">A short statement that explains this point for the reader.</p></div>
    <div class="center" style="width:60px;border-left:.3px solid #ccc;border-right:.3px solid #ccc"><svg class="icon" viewBox="0 0 10 10"><use href="#i-funnel"/></svg><div class="cap" style="font-size:2.6px;margin-top:2px">Your Title Here</div><p class="para" style="margin-top:3px;padding:0 3px">A short statement that explains this point for the reader.</p></div>
    <div class="center" style="width:60px"><svg class="icon" viewBox="0 0 10 10"><use href="#i-gear"/></svg><div class="cap" style="font-size:2.6px;margin-top:2px">Your Title Here</div><p class="para" style="margin-top:3px">A short statement that explains this point for the reader.</p></div>
  </div>
  <span class="foot">©2024 Quorvane. All rights reserved. Confidential information.</span><span class="pg">14</span>
</section>

<section class="slide" style="left:533px;top:467px">
  <div class="rule"></div><span class="brand">QUORVANE</span>
  <div class="ltitle" style="left:17px;top:17px">Simple<br>Text Title<br>Slide</div>
  <div class="abs" style="left:17px;top:56px;font-size:4.6px;color:#555;line-height:1.1">Subtitle text<br>goes here</div>
  <div class="abs cap" style="left:91px;top:17px;font-size:2.3px">What is Lorem Ipsum?</div>
  <p class="abs para" style="left:91px;top:23px;width:116px">Our team explores new oil and gas fields with care, clear data and steady work on every site we open. We plan each well with safety first, share results with partners and keep every deal simple to follow from start to end for every client we serve.</p>
  <div class="abs cap" style="left:91px;top:62px;font-size:2.3px">Why do we use it?</div>
  <p class="abs para" style="left:91px;top:68px;width:116px">Each field study starts with a survey, then a test well, then a full plan for output. We share that plan with partners early so every step is clear, costs stay low and the work stays on time. This keeps our deals open and easy to read.</p>
  <span class="foot">©2024 Quorvane. All rights reserved. Confidential information.</span><span class="pg">15</span>
</section>

<section class="slide" style="left:781px;top:467px">
  <div class="rule"></div><span class="brand">QUORVANE</span>
  <div class="ltitle" style="left:17px;top:20px">The Project<br>Location Number</div>
  <div class="abs cap" style="left:17px;top:50px;width:86px;font-size:2.3px">Write here the subtitle about the project we talking about</div>
  <div class="abs cap" style="left:114px;top:50px;width:86px;font-size:2.3px">Write here the subtitle about the project we talking about</div>
  <p class="abs para" style="left:17px;top:62px;width:86px">Our team explores new oil and gas fields with care, clear data and steady work on every site we open. We plan each well with safety first, share results with partners and keep every deal simple to follow from start to end.</p>
  <p class="abs para" style="left:114px;top:62px;width:86px">Each field study starts with a survey, then a test well, then a full plan for output. We share that plan with partners early so every step is clear and costs stay low for all.</p>
  <span class="foot">©2024 Quorvane. All rights reserved. Confidential information.</span><span class="pg">16</span>
</section>

<!-- Row 5 -->
<section class="slide" style="left:36px;top:607px">
  <div class="rule"></div><span class="brand">QUORVANE</span>
  <div class="title" style="top:19px">One column width text</div>
  <p class="abs para" style="left:17px;right:17px;top:36px">Our team explores new oil and gas fields with care, clear data and steady work on every site we open. We plan each well with safety first, share results with partners and keep every deal simple to follow from start to end for every client we serve.</p>
  <p class="abs para" style="left:17px;top:66px;width:40px">Why do we use it?</p>
  <p class="abs para" style="left:17px;right:17px;top:75px">Each field study starts with a survey, then a test well, then a full plan for output. We share that plan with partners early so every step is clear, costs stay low and the work stays on time. This keeps our deals open and easy to read for all investors.</p>
  <span class="foot">©2024 Quorvane. All rights reserved. Confidential information.</span><span class="pg">17</span>
</section>

<section class="slide" style="left:284px;top:607px">
  <div class="rule"></div><span class="brand">QUORVANE</span>
  <div class="title" style="top:19px">Two column width text</div>
  <p class="abs para" style="left:17px;top:36px;width:88px">Our team explores new oil and gas fields with care, clear data and steady work on every site we open. We plan each well with safety first, share results with partners and keep every deal simple to follow from start to end for every client we serve across the region.</p>
  <p class="abs para" style="left:119px;top:36px;width:88px">Each field study starts with a survey, then a test well, then a full plan for output. We share that plan with partners early so every step is clear, costs stay low and the work stays on time for all.</p>
  <span class="foot">©2024 Quorvane. All rights reserved. Confidential information.</span><span class="pg">18</span>
</section>

<section class="slide" style="left:533px;top:607px">
  <div class="rule"></div><span class="brand">QUORVANE</span>
  <div class="title" style="top:19px">Three column width text</div>
  <p class="abs para" style="left:17px;top:36px;width:56px">Our team explores new oil and gas fields with care, clear data and steady work on every site we open. We plan each well with safety first and share results with partners.</p>
  <p class="abs para" style="left:84px;top:36px;width:56px">Each field study starts with a survey, then a test well, then a full plan for output shared early.</p>
  <p class="abs para" style="left:151px;top:36px;width:56px">We keep every deal simple to follow from start to end, with costs and dates set out plainly for all.</p>
  <span class="foot">©2024 Quorvane. All rights reserved. Confidential information.</span><span class="pg">19</span>
</section>

<section class="slide" style="left:781px;top:607px">
  <div class="rule"></div><span class="brand">QUORVANE</span>
  <div class="title" style="top:19px;left:90px;text-align:left">Infographic slide</div>
  <div class="phase" style="top:30px">Diagnosis phase</div><span class="abs" style="left:66px;top:31px;font-size:2.4px;color:#666">The Problems Identification</span>
  <p class="abs para" style="left:12px;right:12px;top:38px;text-align:left">– Gathering data<br>– Sorting the field reports and survey notes into one clear set of facts.</p>
  <div class="phase dark" style="top:58px">Experimentation phase</div><span class="abs" style="left:66px;top:59px;font-size:2.4px;color:#666">Problem Control</span>
  <p class="abs para" style="left:12px;right:12px;top:66px;text-align:left">– Running test wells and checking each result against the plan set out.<br>– Reviewing output with the team.</p>
  <div class="phase" style="top:86px">Resolution phase</div><span class="abs" style="left:66px;top:87px;font-size:2.4px;color:#666">Error Control</span>
  <p class="abs para" style="left:12px;right:12px;top:94px;text-align:left">– Fixing issues found in testing and setting a steady output plan.<br>– Sharing results with every partner.</p>
  <span class="foot">©2024 Quorvane. All rights reserved. Confidential information.</span><span class="pg">20</span>
</section>

<!-- Row 6 -->
<section class="slide" style="left:36px;top:748px">
  <div class="rule"></div><span class="brand">QUORVANE</span>
  <div class="title" style="top:16px">Solving Problem – Smart Art</div>
  <div class="abs" style="left:14px;right:14px;top:35px;height:72px;display:flex">
    <div style="flex:1;background:#7a7a7a;color:#ddd;display:flex"><div style="width:8px;writing-mode:vertical-rl;transform:rotate(180deg);font-size:3px;font-weight:700;text-align:center">Process One</div><p style="font-size:2.3px;line-height:1.5;padding:4px 2px">Survey the site and gather field data to plan the first test well.</p></div>
    <div style="flex:1;background:var(--cardinal);color:#f5c9cf;display:flex"><div style="width:8px;writing-mode:vertical-rl;transform:rotate(180deg);font-size:3px;font-weight:700;color:#fff;text-align:center">Process Two</div><p style="font-size:2.3px;line-height:1.5;padding:4px 2px">Drill the test well and check the results against the plan.</p></div>
    <div style="flex:1;background:var(--blue);color:#fff;display:flex"><div style="width:8px;writing-mode:vertical-rl;transform:rotate(180deg);font-size:3px;font-weight:700;text-align:center">Process Three</div><p style="font-size:2.3px;line-height:1.5;padding:4px 2px">Set up full output and share the numbers with partners.</p></div>
    <div style="flex:1;background:var(--ink);color:#bbb;display:flex"><div style="width:8px;writing-mode:vertical-rl;transform:rotate(180deg);font-size:3px;font-weight:700;color:#fff;text-align:center">Process Four</div><p style="font-size:2.3px;line-height:1.5;padding:4px 2px">Review the work each quarter and plan the next field.</p></div>
  </div>
  <span class="foot">©2024 Quorvane. All rights reserved. Confidential information.</span><span class="pg">21</span>
</section>

<section class="slide" style="left:284px;top:748px">
  <div class="rule"></div><span class="brand">QUORVANE</span>
  <div class="ltitle" style="left:17px;top:30px">Three<br>Bullet Title<br>Text here</div>
  <p class="abs para" style="left:17px;top:76px;width:64px;text-align:left">A short paragraph that frames the three points and why they matter for this deal.</p>
  <div class="abs" style="left:98px;top:28px;width:110px">
    <div style="display:flex;gap:5px;margin-bottom:9px"><svg class="icon" style="width:8px;height:8px;flex:none" viewBox="0 0 10 10"><use href="#i-check"/></svg><div><div class="cap" style="font-size:2.4px">Your Title Here</div><p class="para" style="text-align:left">A short statement that explains this point for the reader.</p></div></div>
    <div style="display:flex;gap:5px;margin-bottom:9px"><svg class="icon" style="width:8px;height:8px;flex:none" viewBox="0 0 10 10"><use href="#i-check"/></svg><div><div class="cap" style="font-size:2.4px">Your Title Here</div><p class="para" style="text-align:left">A short statement that explains this point for the reader.</p></div></div>
    <div style="display:flex;gap:5px"><svg class="icon" style="width:8px;height:8px;flex:none" viewBox="0 0 10 10"><use href="#i-check"/></svg><div><div class="cap" style="font-size:2.4px">Your Title Here</div><p class="para" style="text-align:left">A short statement that explains this point for the reader.</p></div></div>
  </div>
  <span class="foot">©2024 Quorvane. All rights reserved. Confidential information.</span><span class="pg">22</span>
</section>

<section class="slide" style="left:533px;top:748px">
  <div class="rule"></div><span class="brand">QUORVANE</span>
  <div class="ltitle center" style="left:14px;top:52px;width:66px">Four<br>bullets<br>Title slide</div>
  <div class="abs" style="left:88px;top:32px;width:124px;display:grid;grid-template-columns:1fr 1fr;gap:14px 8px">
    <div><svg class="icon" viewBox="0 0 10 10"><use href="#i-box"/></svg><div style="font-size:3px;font-weight:500">Lorem dummy text</div><p class="para" style="text-align:left">Short copy on this point for the reader.</p></div>
    <div><svg class="icon" viewBox="0 0 10 10"><use href="#i-screen"/></svg><div style="font-size:3px;font-weight:500">Lorem dummy text</div><p class="para" style="text-align:left">Short copy on this point for the reader.</p></div>
    <div><svg class="icon" viewBox="0 0 10 10"><use href="#i-home"/></svg><div style="font-size:3px;font-weight:500">Lorem dummy text</div><p class="para" style="text-align:left">Short copy on this point for the reader.</p></div>
    <div><svg class="icon" viewBox="0 0 10 10"><use href="#i-chat"/></svg><div style="font-size:3px;font-weight:500">Lorem dummy text</div><p class="para" style="text-align:left">Short copy on this point for the reader.</p></div>
  </div>
  <span class="foot">©2024 Quorvane. All rights reserved. Confidential information.</span><span class="pg">23</span>
</section>

<section class="slide" style="left:781px;top:748px">
  <div class="rule"></div><span class="brand">QUORVANE</span>
  <div class="title" style="top:16px">Six bullets slide</div>
  <div class="abs" style="left:20px;right:12px;top:32px;display:grid;grid-template-columns:1fr 1fr 1fr;gap:12px 8px">
    <div><svg class="icon" viewBox="0 0 10 10"><use href="#i-gear"/></svg><div style="font-size:3px;font-weight:500">Lorem dummy text</div><p class="para" style="text-align:left">Short copy on this point for the reader.</p></div>
    <div><svg class="icon" viewBox="0 0 10 10"><use href="#i-home"/></svg><div style="font-size:3px;font-weight:500">Lorem dummy text</div><p class="para" style="text-align:left">Short copy on this point for the reader.</p></div>
    <div><svg class="icon" viewBox="0 0 10 10"><use href="#i-chat"/></svg><div style="font-size:3px;font-weight:500">Lorem dummy text</div><p class="para" style="text-align:left">Short copy on this point for the reader.</p></div>
    <div><svg class="icon" viewBox="0 0 10 10"><use href="#i-wrench"/></svg><div style="font-size:3px;font-weight:500">Lorem dummy text</div><p class="para" style="text-align:left">Short copy on this point for the reader.</p></div>
    <div><svg class="icon" viewBox="0 0 10 10"><use href="#i-box"/></svg><div style="font-size:3px;font-weight:500">Lorem dummy text</div><p class="para" style="text-align:left">Short copy on this point for the reader.</p></div>
    <div><svg class="icon" viewBox="0 0 10 10"><use href="#i-screen"/></svg><div style="font-size:3px;font-weight:500">Lorem dummy text</div><p class="para" style="text-align:left">Short copy on this point for the reader.</p></div>
  </div>
  <span class="foot">©2024 Quorvane. All rights reserved. Confidential information.</span><span class="pg">24</span>
</section>

<!-- Row 7 -->
<section class="slide" style="left:36px;top:888px">
  <div class="rule"></div><span class="brand">QUORVANE</span>
  <div class="title" style="top:14px">Eight bullets slide</div>
  <div class="abs" style="left:9px;right:9px;top:30px;display:grid;grid-template-columns:repeat(4,1fr);gap:10px 6px">
    <div><svg class="icon" viewBox="0 0 10 10"><use href="#i-box"/></svg><div style="font-size:3px;font-weight:500">Lorem dummy text</div><div style="width:5px;height:.5px;background:var(--cardinal);margin:1px 0"></div><p class="para" style="text-align:left">Short copy on this point.</p></div>
    <div><svg class="icon" viewBox="0 0 10 10"><use href="#i-screen"/></svg><div style="font-size:3px;font-weight:500">Lorem dummy text</div><div style="width:5px;height:.5px;background:var(--cardinal);margin:1px 0"></div><p class="para" style="text-align:left">Short copy on this point.</p></div>
    <div><svg class="icon" viewBox="0 0 10 10"><use href="#i-wrench"/></svg><div style="font-size:3px;font-weight:500">Lorem dummy text</div><div style="width:5px;height:.5px;background:var(--cardinal);margin:1px 0"></div><p class="para" style="text-align:left">Short copy on this point.</p></div>
    <div><svg class="icon" viewBox="0 0 10 10"><use href="#i-home"/></svg><div style="font-size:3px;font-weight:500">Lorem dummy text</div><div style="width:5px;height:.5px;background:var(--cardinal);margin:1px 0"></div><p class="para" style="text-align:left">Short copy on this point.</p></div>
    <div><svg class="icon" viewBox="0 0 10 10"><use href="#i-gear"/></svg><div style="font-size:3px;font-weight:500">Lorem dummy text</div><div style="width:5px;height:.5px;background:var(--cardinal);margin:1px 0"></div><p class="para" style="text-align:left">Short copy on this point.</p></div>
    <div><svg class="icon" viewBox="0 0 10 10"><use href="#i-chat"/></svg><div style="font-size:3px;font-weight:500">Lorem dummy text</div><div style="width:5px;height:.5px;background:var(--cardinal);margin:1px 0"></div><p class="para" style="text-align:left">Short copy on this point.</p></div>
    <div><svg class="icon" viewBox="0 0 10 10"><use href="#i-funnel"/></svg><div style="font-size:3px;font-weight:500">Lorem dummy text</div><div style="width:5px;height:.5px;background:var(--cardinal);margin:1px 0"></div><p class="para" style="text-align:left">Short copy on this point.</p></div>
    <div><svg class="icon" viewBox="0 0 10 10"><use href="#i-check"/></svg><div style="font-size:3px;font-weight:500">Lorem dummy text</div><div style="width:5px;height:.5px;background:var(--cardinal);margin:1px 0"></div><p class="para" style="text-align:left">Short copy on this point.</p></div>
  </div>
  <span class="foot">©2024 Quorvane. All rights reserved. Confidential information.</span><span class="pg">25</span>
</section>

<section class="slide" style="left:284px;top:888px">
  <div class="rule"></div><span class="brand">QUORVANE</span>
  <div class="ltitle" style="left:17px;top:22px">Timeline<br>Project<br>slide</div>
  <p class="abs para" style="left:17px;top:60px;width:72px;text-align:left">A short paragraph that frames the project timeline and its main steps. Each stage is set out with a service title and a brief note for the reader.</p>
  <svg class="abs" style="left:116px;top:20px" width="10" height="106" viewBox="0 0 10 106"><line x1="5" y1="12" x2="5" y2="106" stroke="#111" stroke-width=".5" stroke-dasharray="4 3"/></svg>
  <div class="abs" style="left:114px;top:26px;width:96px">
    <div style="display:flex;gap:6px;height:35px"><svg class="icon" style="width:9px;height:9px;background:#fff;flex:none" viewBox="0 0 10 10"><use href="#i-chat"/></svg><div><div class="cap" style="font-size:2.5px">Sept Title</div><p class="para" style="text-align:left;margin-top:2px">Short copy on this stage of work.</p></div></div>
    <div style="display:flex;gap:6px;height:35px"><svg class="icon" style="width:9px;height:9px;background:#fff;flex:none" viewBox="0 0 10 10"><use href="#i-funnel"/></svg><div><div class="cap" style="font-size:2.5px">Sept Title</div><p class="para" style="text-align:left;margin-top:2px">Short copy on this stage of work.</p></div></div>
    <div style="display:flex;gap:6px"><svg class="icon" style="width:9px;height:9px;background:#fff;flex:none" viewBox="0 0 10 10"><use href="#i-box"/></svg><div><div class="cap" style="font-size:2.5px">Sept Title</div><p class="para" style="text-align:left;margin-top:2px">Short copy on this stage of work.</p></div></div>
  </div>
  <span class="foot">©2024 Quorvane. All rights reserved. Confidential information.</span><span class="pg">26</span>
</section>

<section class="slide" style="left:533px;top:888px">
  <div class="rule"></div><span class="brand">QUORVANE</span>
  <div class="ltitle" style="left:17px;top:22px">Timeline<br>Project<br>slide</div>
  <p class="abs para" style="left:17px;top:60px;width:72px;text-align:left">A short paragraph that frames the project timeline and its main steps. Each stage is set out with a service title and a brief note for the reader.</p>
  <svg class="abs" style="left:113px;top:0" width="10" height="100" viewBox="0 0 10 100"><line x1="5" y1="0" x2="5" y2="98" stroke="#111" stroke-width=".5" stroke-dasharray="6 3"/></svg>
  <div class="abs" style="left:111px;top:26px;width:98px">
    <div style="display:flex;gap:6px;height:35px"><svg class="icon" style="width:9px;height:9px;background:#fff;flex:none" viewBox="0 0 10 10"><use href="#i-chat"/></svg><div><div class="cap" style="font-size:2.5px">Service Title</div><p class="para" style="text-align:left;margin-top:2px">Short copy on this service line.</p></div></div>
    <div style="display:flex;gap:6px;height:35px"><svg class="icon" style="width:9px;height:9px;background:#fff;flex:none" viewBox="0 0 10 10"><use href="#i-funnel"/></svg><div><div class="cap" style="font-size:2.5px">Service Title</div><p class="para" style="text-align:left;margin-top:2px">Short copy on this service line.</p></div></div>
    <div style="display:flex;gap:6px"><svg class="icon" style="width:9px;height:9px;background:#fff;flex:none" viewBox="0 0 10 10"><use href="#i-box"/></svg><div><div class="cap" style="font-size:2.5px">Service Title</div><p class="para" style="text-align:left;margin-top:2px">Short copy on this service line.</p></div></div>
  </div>
  <span class="foot">©2024 Quorvane. All rights reserved. Confidential information.</span><span class="pg">27</span>
</section>

<section class="slide" style="left:781px;top:888px">
  <div class="rule"></div><span class="brand">QUORVANE</span>
  <div class="title" style="top:16px">Data Title slide</div>
  <svg class="abs" style="left:0;top:0" width="224" height="126" viewBox="0 0 224 126">
    <text x="112" y="40" font-size="3" fill="#999" text-anchor="middle" font-family="Montserrat, sans-serif">Chart Title</text>
    <g stroke="#eee" stroke-width=".3"><line x1="20" y1="46" x2="210" y2="46"/><line x1="20" y1="56" x2="210" y2="56"/><line x1="20" y1="66" x2="210" y2="66"/><line x1="20" y1="76" x2="210" y2="76"/><line x1="20" y1="86" x2="210" y2="86"/><line x1="20" y1="96" x2="210" y2="96"/></g>
    <line x1="20" y1="106" x2="210" y2="106" stroke="#bbb" stroke-width=".3"/>
    <g fill="#c8102e"><rect x="27" y="68" width="6" height="38"/><rect x="58" y="84" width="6" height="22"/><rect x="89" y="81" width="6" height="25"/><rect x="120" y="74" width="6" height="32"/><rect x="151" y="84" width="6" height="22"/><rect x="182" y="70" width="6" height="36"/></g>
    <g fill="#111"><rect x="35" y="85" width="6" height="21"/><rect x="66" y="72" width="6" height="34"/><rect x="97" y="60" width="6" height="46"/><rect x="128" y="70" width="6" height="36"/><rect x="159" y="90" width="6" height="16"/><rect x="190" y="78" width="6" height="28"/></g>
    <polyline points="34,76 65,84 96,88 127,82 158,76 189,62" fill="none" stroke="#8e44ad" stroke-width=".5"/>
    <g font-size="2.2" fill="#999" text-anchor="middle" font-family="Montserrat, sans-serif"><text x="34" y="111">Category 1</text><text x="65" y="111">Category 2</text><text x="96" y="111">Category 3</text><text x="127" y="111">Category 4</text><text x="158" y="111">Category 5</text><text x="189" y="111">Category 6</text></g>
    <g font-size="2" fill="#777" font-family="Montserrat, sans-serif"><rect x="88" y="114" width="3" height="1.5" fill="#c8102e"/><text x="92" y="115.5">Series 1</text><rect x="104" y="114" width="3" height="1.5" fill="#111"/><text x="108" y="115.5">Series 2</text><line x1="120" y1="114.8" x2="123" y2="114.8" stroke="#8e44ad" stroke-width=".5"/><text x="124" y="115.5">Series 3</text></g>
  </svg>
  <span class="foot">©2024 Quorvane. All rights reserved. Confidential information.</span><span class="pg">28</span>
</section>

<!-- Row 8 -->
<section class="slide" style="left:36px;top:1028px">
  <div class="rule"></div><span class="brand">QUORVANE</span>
  <div class="title" style="top:16px">Data Title slide</div>
  <div class="abs" style="left:17px;top:37px;font-size:4px;font-weight:500">Subtitle slide goes here</div>
  <p class="abs para" style="left:17px;top:45px;width:62px;text-align:left">• Our team explores new oil and gas fields with care, clear data and steady work on every site we open. We plan each well with safety first and share results with partners.<br>• Every deal is simple to follow from start to end.</p>
  <svg class="abs" style="left:0;top:0" width="224" height="126" viewBox="0 0 224 126">
    <text x="148" y="40" font-size="3" fill="#999" text-anchor="middle" font-family="Montserrat, sans-serif">Chart Title</text>
    <g stroke="#eee" stroke-width=".3"><line x1="90" y1="46" x2="210" y2="46"/><line x1="90" y1="56" x2="210" y2="56"/><line x1="90" y1="66" x2="210" y2="66"/><line x1="90" y1="76" x2="210" y2="76"/><line x1="90" y1="86" x2="210" y2="86"/></g>
    <line x1="90" y1="96" x2="210" y2="96" stroke="#bbb" stroke-width=".3"/>
    <g fill="#c8102e"><rect x="98" y="66" width="5" height="30"/><rect x="128" y="72" width="5" height="24"/><rect x="158" y="80" width="5" height="16"/><rect x="188" y="60" width="5" height="36"/></g>
    <g fill="#bbb"><rect x="104" y="83" width="5" height="13"/><rect x="134" y="58" width="5" height="38"/><rect x="164" y="83" width="5" height="13"/><rect x="194" y="73" width="5" height="23"/></g>
    <g fill="#111"><rect x="110" y="78" width="5" height="18"/><rect x="140" y="76" width="5" height="20"/><rect x="170" y="68" width="5" height="28"/><rect x="200" y="57" width="5" height="39"/></g>
    <g font-size="2.2" fill="#999" text-anchor="middle" font-family="Montserrat, sans-serif"><text x="106" y="101">Category 1</text><text x="136" y="101">Category 2</text><text x="166" y="101">Category 3</text><text x="196" y="101">Category 4</text></g>
    <g font-size="2" fill="#777" font-family="Montserrat, sans-serif"><rect x="128" y="104" width="1.5" height="1.5" fill="#c8102e"/><text x="130.5" y="105.5">Series 1</text><rect x="140" y="104" width="1.5" height="1.5" fill="#bbb"/><text x="142.5" y="105.5">Series 2</text><rect x="152" y="104" width="1.5" height="1.5" fill="#111"/><text x="154.5" y="105.5">Series 3</text></g>
  </svg>
  <span class="foot">©2024 Quorvane. All rights reserved. Confidential information.</span><span class="pg">29</span>
</section>

<section class="slide" style="left:284px;top:1028px">
  <div class="rule"></div><span class="brand">QUORVANE</span>
  <div class="title" style="top:16px">Data multiple pie slide</div>
  <svg class="abs" style="left:0;top:34px" width="224" height="40" viewBox="0 0 224 40">
    <g fill="none" stroke-width="2.2">
      <circle cx="36" cy="20" r="15" stroke="#ddd"/><circle cx="36" cy="20" r="15" stroke="#1d2d4a" stroke-dasharray="47.1 94.2" transform="rotate(-90 36 20)"/>
      <circle cx="85" cy="20" r="15" stroke="#ddd"/><circle cx="85" cy="20" r="15" stroke="#c8102e" stroke-dasharray="28.3 94.2" transform="rotate(-90 85 20)"/>
      <circle cx="134" cy="20" r="15" stroke="#ddd"/><circle cx="134" cy="20" r="15" stroke="#1d2d4a" stroke-dasharray="9.4 94.2" transform="rotate(-90 134 20)"/>
      <circle cx="183" cy="20" r="15" stroke="#ddd"/><circle cx="183" cy="20" r="15" stroke="#c8102e" stroke-dasharray="37.7 94.2" transform="rotate(-90 183 20)"/>
    </g>
    <g font-size="5" font-weight="700" text-anchor="middle" font-family="Montserrat, sans-serif"><text x="36" y="22">50%</text><text x="85" y="22">30%</text><text x="134" y="22">10%</text><text x="183" y="22">40%</text></g>
  </svg>
  <div class="abs" style="left:14px;right:14px;top:79px;display:flex;justify-content:space-between">
    <div class="center" style="width:42px"><div style="font-size:3.4px;font-weight:700">Data title here</div><p class="para center" style="margin-top:2px">Short copy on what this figure shows.</p></div>
    <div class="center" style="width:42px"><div style="font-size:3.4px;font-weight:700">Data title here</div><p class="para center" style="margin-top:2px">Short copy on what this figure shows.</p></div>
    <div class="center" style="width:42px"><div style="font-size:3.4px;font-weight:700">Data title here</div><p class="para center" style="margin-top:2px">Short copy on what this figure shows.</p></div>
    <div class="center" style="width:42px"><div style="font-size:3.4px;font-weight:700">Data title here</div><p class="para center" style="margin-top:2px">Short copy on what this figure shows.</p></div>
  </div>
  <span class="foot">©2024 Quorvane. All rights reserved. Confidential information.</span><span class="pg">30</span>
</section>

<section class="slide" style="left:533px;top:1028px">
  <div class="rule"></div><span class="brand">QUORVANE</span>
  <div class="title" style="top:16px">Data multiple pie slide</div>
  <svg class="abs" style="left:0;top:0" width="224" height="126" viewBox="0 0 224 126">
    <g fill="none" stroke-width="1.6">
      <circle cx="34" cy="56" r="10" stroke="#eee"/><circle cx="34" cy="56" r="10" stroke="#111" stroke-dasharray="6.3 62.8" transform="rotate(-90 34 56)"/>
      <circle cx="72" cy="84" r="10" stroke="#eee"/><circle cx="72" cy="84" r="10" stroke="#c8102e" stroke-dasharray="22 62.8" transform="rotate(-90 72 84)"/>
      <circle cx="110" cy="56" r="10" stroke="#eee"/><circle cx="110" cy="56" r="10" stroke="#c8102e" stroke-dasharray="56.5 62.8" transform="rotate(-90 110 56)"/>
      <circle cx="148" cy="84" r="10" stroke="#eee"/><circle cx="148" cy="84" r="10" stroke="#111" stroke-dasharray="14.4 62.8" transform="rotate(-90 148 84)"/>
      <circle cx="186" cy="56" r="10" stroke="#eee"/><circle cx="186" cy="56" r="10" stroke="#111" stroke-dasharray="47.1 62.8" transform="rotate(-90 186 56)"/>
    </g>
    <g font-size="4.2" font-weight="700" text-anchor="middle" font-family="Montserrat, sans-serif"><text x="34" y="57.5">10%</text><text x="72" y="85.5">35%</text><text x="110" y="57.5">90%</text><text x="148" y="85.5">23%</text><text x="186" y="57.5">75%</text></g>
  </svg>
  <div class="abs center" style="left:52px;width:40px;top:44px"><div style="font-size:3.2px;font-weight:700;color:var(--navy)">Data title here</div><p class="para center">Short copy on what this figure shows.</p></div>
  <div class="abs center" style="left:128px;width:40px;top:44px"><div style="font-size:3.2px;font-weight:700;color:var(--navy)">Data title here</div><p class="para center">Short copy on what this figure shows.</p></div>
  <div class="abs center" style="left:14px;width:40px;top:72px"><div style="font-size:3.2px;font-weight:700;color:var(--navy)">Data title here</div><p class="para center">Short copy on what this figure shows.</p></div>
  <div class="abs center" style="left:90px;width:40px;top:72px"><div style="font-size:3.2px;font-weight:700;color:var(--navy)">Data title here</div><p class="para center">Short copy on what this figure shows.</p></div>
  <div class="abs center" style="left:166px;width:40px;top:72px"><div style="font-size:3.2px;font-weight:700;color:var(--navy)">Data title here</div><p class="para center">Short copy on what this figure shows.</p></div>
  <span class="foot">©2024 Quorvane. All rights reserved. Confidential information.</span><span class="pg">31</span>
</section>

<section class="slide" style="left:781px;top:1028px">
  <div class="rule"></div><span class="brand">QUORVANE</span>
  <div class="title" style="top:16px">Table Data Title slide</div>
  <table class="data">
    <tr><th style="background:none"></th><th>Column 1</th><th>Column 2</th><th>Column 3</th><th>Column 4</th><th>Column 5</th><th>Column 6</th></tr>
    <tr><td>Fila 01</td><td>48</td><td>66</td><td>75</td><td>45</td><td>66</td><td>34</td></tr>
    <tr><td>Fila 02</td><td>35</td><td>75</td><td>89</td><td>58</td><td>48</td><td>66</td></tr>
    <tr><td>Fila 03</td><td>66</td><td>34</td><td>55</td><td>35</td><td>35</td><td>75</td></tr>
    <tr><td>Fila 04</td><td>55</td><td>70</td><td>84</td><td>52</td><td>55</td><td>35</td></tr>
    <tr><td>Fila 05</td><td>48</td><td>66</td><td>75</td><td>45</td><td>66</td><td>34</td></tr>
    <tr><td>Fila 06</td><td>35</td><td>75</td><td>89</td><td>58</td><td>48</td><td>66</td></tr>
    <tr><td>Fila 07</td><td>66</td><td>34</td><td>55</td><td>35</td><td>35</td><td>75</td></tr>
    <tr><td>Fila 08</td><td>55</td><td>70</td><td>84</td><td>52</td><td>55</td><td>35</td></tr>
    <tr><td>Fila 09</td><td>48</td><td>66</td><td>75</td><td>45</td><td>66</td><td>34</td></tr>
    <tr class="total"><td>Total Columns</td><td>456</td><td>556</td><td>681</td><td>425</td><td>474</td><td>454</td></tr>
  </table>
  <span class="foot">©2024 Quorvane. All rights reserved. Confidential information.</span><span class="pg">32</span>
</section>

</body>
</html>
```